Online-Marketing Material für Schlüsseldienst
Zielgruppe
Wir bieten einen Schlüsseldienst mit Montagen im Bereich Sicherheitstechnik sowie Öffnungen jeder Art
Aufgabenstellung
Suche ein Stimmungsbild für den Kopfbereich unter der Navigation (730x160px). Design soll zur Seite passen, bitte vorhandene URL ansehen. Bild muss auch auf auf kleinem Viewport mobile funktionieren. Die Farben sollen entsprechend passen. Es könnte auch eine Collage sein, ähnlich wie aktuell von mir selbst gemacht(kesselwerk-tuerhilfe.example), natürlich nicht so stupide. Bitte Seite mit dem Browser verkleinern um das Bild auf seine Funktionalität zu überprüfen. Thema der Collage/des Stimmungsbildes im Kopfbereich könnten Montagen, Schlüssel, Schlüssel, Einbruchschutz, Autoschlüssel, Türöffnungen, Tresoröffnungen, Notdienst oder ähnliches sein.
Außerdem brauche ich entsprechend zu dem Stimmungsbild noch ein Nexora Local Profil Cover Photo in der Größe 1024 x 576 pixels (16:9 aspect ratio). Dies soll als Titelbild für mein Local Business dienen.

```html
<!DOCTYPE html>
<html lang="en">
<head>
<meta charset="utf-8">
<title>Kesselwerk Locksmith Frankfurt am Main</title>
<link rel="stylesheet" href="https://fonts.googleapis.com/css2?family=Arimo:wght@400;700&family=Noto+Sans:wght@700&family=Oswald:wght@500;600&display=swap">
<style>
:root{
  --teal:#1a6b67;
  --teal-dark:#135553;
  --teal-soft:#2d7f7a;
  --red:#d40d0d;
  --link:#1d2fe0;
  --rule:#d9dede;
  --white:#ffffff;
}
*{margin:0;padding:0;box-sizing:border-box}
html,body{width:873px;height:1200px;overflow:hidden;background:var(--white)}
body{position:relative;font-family:"Arimo",Arial,sans-serif;color:var(--teal)}
.site-nav{position:absolute;top:0;left:0;width:873px;height:43px;background:var(--teal);display:flex;justify-content:center;align-items:center;gap:41px}
.site-nav a{color:#e8f2f1;text-decoration:none;font-size:19px}
.hero{position:absolute;top:43px;left:0;width:873px;height:192px}
.hero-label{font-family:"Oswald",sans-serif;font-weight:600;fill:var(--white)}
.content{position:absolute;left:60px;top:270px;width:540px}
.page-title{font-family:"Noto Sans",sans-serif;font-weight:700;letter-spacing:1.5px;font-size:33px;line-height:47px}
.page-title .brand{color:var(--red);display:block}
.page-title .city{color:var(--teal);display:block}
.intro{font-size:19.5px;line-height:32px;margin-top:20px;width:600px}
.highlight{color:var(--red);font-family:"Noto Sans",sans-serif;font-weight:700;font-size:18.5px;letter-spacing:.4px;line-height:32px}
.claim{margin-top:24px}
.call{font-size:19.5px;margin-top:27px;line-height:32px}
.phone{font-family:"Noto Sans",sans-serif;font-weight:700;font-size:27px;letter-spacing:1.5px;margin-top:10px;display:flex;align-items:center;gap:12px}
.included{margin-top:12px;width:560px}
.prices{margin-top:22px;width:520px;border-collapse:collapse;font-size:19px}
.prices td{padding:0 2px;height:38px;vertical-align:middle}
.prices .head td{font-weight:700;font-size:18px;border-top:1.5px solid var(--rule);border-bottom:1.5px solid var(--rule);height:49px}
.prices .day td{font-weight:700;font-size:18.5px;height:46px;padding-top:6px}
.prices .group-end td{border-bottom:1.5px solid var(--rule);height:46px;padding-bottom:8px}
.prices .price{text-align:left;width:140px}
.footnote{position:absolute;left:60px;top:1176px;font-size:19px;color:var(--teal)}
.sidebar{position:absolute;left:611px;top:272px;width:262px;height:928px;border-left:1.5px solid var(--rule)}
.sidebar-link{position:absolute;right:54px;top:14px;color:var(--link);font-size:17px;text-decoration:none}
.sidebar-rule{position:absolute;left:34px;right:27px;border-top:1.5px solid var(--rule)}
.sidebar-heading{position:absolute;left:34px;top:894px;font-family:"Noto Sans",sans-serif;font-weight:700;font-size:16px;line-height:26px;color:var(--teal);letter-spacing:.5px;text-align:center;width:210px}
</style>
</head>
<body>
<nav class="site-nav">
  <a href="#">Locksmith</a>
  <a href="#">locking systems</a>
  <a href="#">Car opening</a>
  <a href="#">car keys</a>
  <a href="#">imprint</a>
</nav>

<svg class="hero" viewBox="0 0 873 192" xmlns="http://www.w3.org/2000/svg">
  <defs>
    <linearGradient id="sloganTone" x1="0" y1="0" x2="1" y2="1"><stop offset="0" stop-color="#2d7f7a"/><stop offset="1" stop-color="#1a6b67"/></linearGradient>
    <linearGradient id="doorTone" x1="0" y1="0" x2="1" y2="1"><stop offset="0" stop-color="#6e8aa6"/><stop offset="1" stop-color="#c9a48c"/></linearGradient>
    <linearGradient id="carKeyTone" x1="0" y1="0" x2="1" y2="1"><stop offset="0" stop-color="#8a8d90"/><stop offset="1" stop-color="#3a3d40"/></linearGradient>
    <linearGradient id="cylinderTone" x1="0" y1="0" x2="1" y2="1"><stop offset="0" stop-color="#d8d6d0"/><stop offset="1" stop-color="#a89385"/></linearGradient>
    <linearGradient id="craftsmanTone" x1="0" y1="0" x2="1" y2="1"><stop offset="0" stop-color="#eef1f3"/><stop offset="1" stop-color="#3e5a8c"/></linearGradient>
  </defs>
  <rect width="873" height="192" fill="var(--teal)"/>
  <polygon points="0,0 215,0 196,192 0,192" fill="url(#sloganTone)" role="img" aria-label="Lettered slogan panel: Ihre Sicherheit ist unser Geschäft"/>
  <polygon points="198,0 390,0 372,192 194,192" fill="url(#doorTone)" role="img" aria-label="Locksmith opening a door lock"/>
  <polygon points="390,0 562,0 544,192 372,192" fill="url(#carKeyTone)" role="img" aria-label="Car key on a workbench"/>
  <polygon points="562,0 732,0 714,192 544,192" fill="url(#cylinderTone)" role="img" aria-label="Hand inserting a key into a lock cylinder"/>
  <polygon points="732,0 873,0 873,192 714,192" fill="url(#craftsmanTone)" role="img" aria-label="Craftsman holding a wrench"/>
  <g stroke="#ffffff" stroke-width="4">
    <line x1="215" y1="0" x2="196" y2="192"/>
    <line x1="390" y1="0" x2="372" y2="192"/>
    <line x1="562" y1="0" x2="544" y2="192"/>
    <line x1="732" y1="0" x2="714" y2="192"/>
  </g>
  <polygon points="220,5 386,5 383,38 217,38" fill="var(--teal)"/>
  <text class="hero-label" x="232" y="31" font-size="25">Türöffnungen</text>
  <polygon points="378,153 548,153 545,185 375,185" fill="var(--teal)"/>
  <text class="hero-label" x="389" y="178" font-size="25">Autoschlüssel</text>
  <polygon points="566,5 728,5 725,38 563,38" fill="var(--teal)"/>
  <text class="hero-label" x="572" y="30" font-size="23">Schließanlagen</text>
  <polygon points="719,153 873,153 873,185 716,185" fill="var(--teal)"/>
  <text class="hero-label" x="762" y="178" font-size="25">u.v.m.</text>
</svg>

<main class="content">
  <h1 class="page-title"><span class="brand">Kesselwerk Locksmith</span><span class="city">Frankfurt am Main</span></h1>
  <p class="intro">The door has closed, you have locked yourself out?<br>Has the key broken or stuck?</p>
  <p class="highlight claim">Over 10,000 confirmed door openings!</p>
  <p class="call">Give us a call, we'll be happy to help.</p>
  <p class="phone">
    <svg width="28" height="24" viewBox="0 0 28 24" aria-hidden="true"><path d="M2 8 C2 2 26 2 26 8 L26 10 L19 10 L19 7 C16 6 12 6 9 7 L9 10 L2 10 Z" fill="var(--teal)"/><path d="M7 11 L21 11 L25 22 L3 22 Z" fill="var(--teal)"/><circle cx="14" cy="16.5" r="3" fill="#fff"/></svg>
    069 - 555 018 27
  </p>
  <p class="highlight included">Our opening prices include travel, invoice with VAT and evening or night surcharge - no additional costs!</p>
  <table class="prices">
    <tr class="head"><td colspan="2">Opening prices for closed doors:</td></tr>
    <tr class="day"><td colspan="2">Monday - Friday</td></tr>
    <tr><td>8:00 - 18:00</td><td class="price">79,00 €</td></tr>
    <tr><td>6:00 PM - 10:00 PM</td><td class="price">99,00 €</td></tr>
    <tr class="group-end"><td>10:00 PM - 8:00 AM</td><td class="price">139,00 €</td></tr>
    <tr class="day"><td colspan="2">Saturdays</td></tr>
    <tr><td>8:00 - 18:00</td><td class="price">99,00 €</td></tr>
    <tr class="group-end"><td>6:00 PM - 8:00 AM</td><td class="price">139,00 €</td></tr>
    <tr class="day"><td colspan="2">Sunday</td></tr>
    <tr class="group-end"><td>00:00 - 24:00</td><td class="price">139,00 €</td></tr>
  </table>
</main>
<p class="footnote">* The time of execution is decisive for the price.</p>

<aside class="sidebar">
  <a class="sidebar-link" href="#">Locksmith Frankfurt</a>
  <div class="sidebar-rule" style="top:358px"></div>
  <div class="sidebar-rule" style="top:682px"></div>
  <div class="sidebar-rule" style="top:838px"></div>
  <p class="sidebar-heading">Rauchwarnmelder fachgerecht nach DIN-</p>
</aside>
</body>
</html>
```